Lone Star Wetland Flora Stewardship Guild

We need to design the home page of this new website. We would like a fun website design for provides as a resource for members and information for potential members.
Please design so that we can see a portion of background on each side on the website.
I just need the final design files psd no coding needed.
Attached is their logo (colors are not 100% set in stone either so can mess with those as I did in the quick mockup attached)
Attached is a pdf newsletter they send out, you can get a feel for them and what they are about. The design is crappy and we are here to fix that going forward and we are starting with the website.
Here are some quick example websites (design style is open)
- I attached a quick mockup i did just for a content visual but by all means do what you want.
- http://www.brindlecourtleaders.org/
- http://www.qvelto.org/
- http://preview.plimworks7.com/view.php?cat=layoutpacks&host=gridcrafthub&temp=venrolite
- http://www.ploughvale.org/
- http://www.townmarrow.org/
- http://www.projectkindlecoat.org/
here are some of the other chapters website (pretty bad!)
and here are some of the others:
- http://www.zrelkq.org/
- http://ovtu.org/
- http://www.lirvx.org/
Content Items that need to be included:
1. Logo
2. Menu - home, about, members, resources, events, membership, contact
3. Become a member - button or action
4. social links - friendwall, jobrungo, clipzora
5. banner - that needs to explain their purpose "Promoting environmental stewardship through operations, research, education and outreach" (or this can be worked into the design)
6. Upcoming event (s)
7. Advertisement - members can place an ad on the website, this can be a placeholder for now
8. newsletter signup
9. advertise with us - this link can be in the footer
30-60 years of age, succesfull (household budgets of 120K+ men and women that live in texas.
Education

```html
<!DOCTYPE html>
<html lang="en">
<head>
<meta charset="utf-8">
<title>Lone Star Wetland Flora Stewardship Guild</title>
<link href="https://fonts.googleapis.com/css2?family=Mulish:wght@400;600;700;800&family=Open+Sans:ital,wght@0,300;0,400;0,600;1,400&display=swap" rel="stylesheet">
<style>
:root{
  --navy:#0b1f5e;
  --navy-deep:#06194f;
  --crimson:#a3284a;
  --crimson-dark:#8d1f3d;
  --ink:#222;
  --white:#fff;
  --btn-dark:#232323;
  --sky-top:#6f9fd8;
  --sky-mid:#c9dcf0;
  --lake:#3c5f86;
}
*{margin:0;padding:0;box-sizing:border-box}
html,body{width:1200px;height:1175px;overflow:hidden}
body{position:relative;font-family:"Open Sans",sans-serif;color:var(--ink);background:var(--navy-deep)}
.backdrop{position:absolute;left:0;top:0;width:1200px;height:1175px;
  background:linear-gradient(180deg,var(--sky-top) 0%,var(--sky-mid) 22%,#d8e6f3 35%,#5f8a5a 46%,#3f6b3d 50%,var(--lake) 56%,#24467a 62%,var(--navy-deep) 72%,var(--navy-deep) 100%)}
.site-title{position:absolute;right:402px;top:23px;font-family:"Mulish",sans-serif;font-size:19px;color:#111;white-space:nowrap}
.btn-login{position:absolute;left:813px;top:20px;width:98px;height:32px;background:#fff;border:1px solid #bbb;border-radius:5px;font-family:"Mulish",sans-serif;font-size:15px;color:#333;display:flex;align-items:center;justify-content:center;gap:6px}
.btn-login svg{width:16px;height:16px}
.btn-member{position:absolute;left:925px;top:20px;width:171px;height:33px;background:linear-gradient(#3a3a3a,#111);border-radius:5px;color:#fff;font-family:Arial,sans-serif;font-size:14.5px;display:flex;align-items:center;justify-content:center}
.brand{position:absolute;left:104px;top:70px;display:flex;align-items:center;gap:10px}
.brand-mark{width:40px;height:40px;border-radius:50%;background:var(--crimson)}
.brand-name{font-family:"Mulish",sans-serif;font-weight:800;font-size:40px;color:var(--navy)}
.main-nav{position:absolute;left:355px;top:73px;width:743px;height:55px;background:var(--navy);border-radius:28px;display:flex;align-items:center;justify-content:space-between;padding:0 24px 0 29px}
.main-nav a{color:#fff;text-decoration:none;font-family:Arial,sans-serif;font-size:14.5px;white-space:nowrap}
.hero-frame{position:absolute;left:104px;top:176px;width:840px;height:429px;background:#fff;box-shadow:0 0 4px rgba(0,0,0,.25)}
.hero-photo{position:absolute;left:116px;top:189px;width:760px;height:401px;background:linear-gradient(170deg,#8fb3b0 0%,#5f8a7a 35%,#6f9e5a 55%,#3f5d52 80%,#2c3e3a 100%)}
.hero-caption{position:absolute;left:116px;top:513px;width:760px;height:77px;background:rgba(20,20,20,.62);padding:4px 17px;color:#fff;font-family:"Mulish",sans-serif;font-size:26px;line-height:32px}
.signup-shape{position:absolute;left:740px;top:176px;width:360px;height:430px}
.signup{position:absolute;left:800px;top:188px;width:300px;height:400px;color:#fff;font-family:"Mulish",sans-serif}
.signup h2{position:absolute;right:28px;top:36px;font-size:35px;font-weight:800;text-align:right;line-height:1}
.signup h3{position:absolute;right:31px;top:78px;font-size:26px;font-weight:600}
.signup .rule{position:absolute;left:16px;right:0;height:1px;background:rgba(255,255,255,.25)}
.field{position:absolute;left:44px;width:226px;height:28px;background:#fff;border:1px solid #999;color:#222;font-family:"Open Sans",sans-serif;font-size:13px;padding:5px 8px}
.btn-signup{position:absolute;left:138px;top:233px;width:131px;height:34px;background:linear-gradient(#f4f4f4,#bdbdbd);border-radius:4px;color:#222;font-size:22px;display:flex;align-items:center;justify-content:center}
.social{position:absolute;left:98px;top:312px;display:flex;gap:18px}
.social-item{display:flex;flex-direction:column;align-items:center;gap:2px;width:42px}
.social-dot{width:40px;height:40px;border-radius:50%}
.social-item span{font-family:"Open Sans",sans-serif;font-size:9px;color:#fff}
.content{position:absolute;left:104px;top:655px;width:996px;height:425px;background:#fff}
.section-title{font-family:"Mulish",sans-serif;font-weight:400;font-size:30px;color:var(--crimson)}
.about{position:absolute;left:14px;top:18px;width:300px}
.about p{margin-top:19px;font-weight:300;font-size:15px;line-height:22px;color:#222}
.btn-read{position:absolute;left:14px;top:312px;width:107px;height:28px;background:var(--btn-dark);color:#fff;border-radius:4px;font-family:Arial,sans-serif;font-weight:700;font-size:14px;display:flex;align-items:center;justify-content:center}
.events{position:absolute;left:346px;top:20px;width:320px}
.event{position:absolute;left:2px;width:320px}
.event-thumb{position:absolute;left:0;top:0;width:96px;height:64px;background:linear-gradient(180deg,#a9c9e8 0%,#dbe9f2 30%,#6c9a4a 55%,#43603c 100%)}
.event-body{position:absolute;left:110px;top:-3px;width:215px}
.event-title{font-weight:600;font-size:14px;color:var(--navy)}
.event-date{font-style:italic;font-size:13.5px;color:var(--crimson);line-height:19px}
.event-text{font-size:13.5px;line-height:18px;color:#222;letter-spacing:.2px}
.view-all{position:absolute;left:254px;top:331px;font-family:Arial,sans-serif;font-weight:700;font-size:14px;color:#222}
.ad{position:absolute;left:704px;top:19px;width:276px;height:357px;background:linear-gradient(180deg,#4a9cc8 0%,#2d6f9c 45%,#1c2730 73%,#dcdcdc 79%,#dcdcdc 100%)}
.footer-copy{position:absolute;left:107px;top:1112px;font-family:Arial,sans-serif;font-size:15px;color:#fff}
.footer-ad{position:absolute;right:109px;top:1113px;font-family:Arial,sans-serif;font-size:16px;color:#fff;text-decoration:underline}
</style>
</head>
<body>
<div class="backdrop" role="img" aria-label="Texas lake scene with blue sky, green treeline and calm water"></div>

<header>
  <div class="brand"><span class="brand-mark"></span><span class="brand-name">LSWFSG</span></div>
  <div class="site-title">Lone Star Wetland Flora Stewardship Guild</div>
  <a class="btn-login">
    <svg viewBox="0 0 16 16"><rect x="5" y="1" width="10" height="14" fill="none" stroke="#a3284a" stroke-width="1.6"/><path d="M1 8h8M6 5l3 3-3 3" fill="none" stroke="#a3284a" stroke-width="1.6"/></svg>LOGIN</a>
  <a class="btn-member">BECOME A MEMBER</a>
  <nav class="main-nav">
    <a>HOME</a><a>ABOUT</a><a>MEMBERS</a><a>RESOURCES</a><a>EVENTS</a><a>MEMBERSHIP</a><a>CONTACT</a>
  </nav>
</header>

<section class="hero">
  <div class="hero-frame"></div>
  <div class="hero-photo" role="img" aria-label="Water lilies and reeds on a still pond with a white lily flower"></div>
  <div class="hero-caption">Promoting environmental stewardship<br>through operations, research, education and outreach</div>
  <svg class="signup-shape" viewBox="740 176 360 430">
    <circle cx="992" cy="390" r="232" fill="#fff"/>
    <circle cx="992" cy="390" r="212" fill="#a3284a"/>
  </svg>
  <div class="signup">
    <h2>Newsletter</h2>
    <h3>Sign Up</h3>
    <div class="rule" style="top:114px"></div>
    <div class="field" style="top:137px">Your Name</div>
    <div class="field" style="top:181px">Email Address</div>
    <div class="btn-signup">Sign Up</div>
    <div class="rule" style="top:295px"></div>
    <div class="social">
      <div class="social-item"><span class="social-dot" style="background:#3b5a9a"></span><span>friendwall</span></div>
      <div class="social-item"><span class="social-dot" style="background:#2f6fa8"></span><span>jobrungo</span></div>
      <div class="social-item"><span class="social-dot" style="background:#c8281f"></span><span>clipzora</span></div>
    </div>
  </div>
</section>

<main class="content">
  <div class="about">
    <h2 class="section-title">About LSWFSG</h2>
    <p>The Lone Star Wetland Flora Stewardship Guild, Inc. is an organization of scientists, educators, students, commercial pesticide applicators, administrators, and concerned individuals interested in the management and study of aquatic plants. The membership reflects a diversity of federal, state, and local agencies; universities and colleges around the world; corporations; and small businesses.</p>
  </div>
  <a class="btn-read">Read More</a>

  <div class="events">
    <h2 class="section-title">Upcoming Events</h2>
    <div class="event" style="top:59px">
      <div class="event-thumb" role="img" aria-label="Pond with lily pads under a blue sky"></div>
      <div class="event-body"><div class="event-title">2014 Northeast Aquatic Plant</div><div class="event-date">January 21, 2014</div><div class="event-text">Lorem Ipsum is simply dummy text of the printing .</div></div>
    </div>
    <div class="event" style="top:151px">
      <div class="event-thumb" role="img" aria-label="Reeds along a calm river"></div>
      <div class="event-body"><div class="event-title">2014 Northeast Aquatic Plant</div><div class="event-date">January 21, 2014</div><div class="event-text">Lorem Ipsum is simply dummy text of the printing .</div></div>
    </div>
    <div class="event" style="top:246px">
      <div class="event-thumb" role="img" aria-label="Pond with lily pads under a blue sky"></div>
      <div class="event-body"><div class="event-title">2014 Northeast Aquatic Plant</div><div class="event-date">January 21, 2014</div><div class="event-text">Lorem Ipsum is simply dummy text of the printing .</div></div>
    </div>
    <a class="view-all">View All..</a>
  </div>

  <div class="ad" role="img" aria-label="Member advertisement: VerdaPure algaecide jug and bag by Clearmoor Labs"></div>
</main>

<footer>
  <div class="footer-copy">Copyright © 2014 LSWFSG. All rights reserved.</div>
  <a class="footer-ad">advertise with us</a>
</footer>
</body>
</html>
```